Retail Sign for Houseplant Campaign

Sign will measure 3 to 4 foot tall by 22.2inches and place on rolling racks of houseplants for a retail promotion in The Brickfield Yard. The theme of the promotion will be "New Year, New You!" Selling points which should be on the sign are Houseplants give you a taste of nature, Houseplants boost air quality inside your home, Indoor plants reduce anxiety, Indoor plants make you more productive, Houseplants improve your concentration and memory.
Updates

Target Market(s)

People who love plants

Industry/Entity Type

Horticulture/ retail

Colors
00AB8E
00BBA5
67D7C9
C6EFE9
E9F9F6
59FF00
82FF00
B8FF75
E3FFCB
F4FFEA
FFF300
FFF600
FEFA6F
FFFEC7
FFFEE8

Requirements
Must have
• Must feel energetic and encourage people to buy plants. Should include 1-2 photos and the selling points listed

```html
<!DOCTYPE html>
<html lang="en">
<head>
<meta charset="utf-8">
<title>New Year, New You! – Houseplant Sign</title>
<link rel="stylesheet" href="https://fonts.googleapis.com/css2?family=Oswald:wght@500&family=Dancing+Script:wght@700&family=Roboto+Condensed:wght@300&family=Montserrat:wght@400;500&display=swap">
<style>
  :root {
    --paper: #ffffff;
    --leaf-green: #6cb34a;
    --teal: #22a89a;
    --teal-light: #67c7bd;
    --sun-yellow: #f6f28c;
    --line-yellow: #e4e86a;
    --sage: #dfeac4;
    --forest: #4a5c2e;
    --ink: #3d3d3d;
    --brick: #d8692c;
  }
  * { margin: 0; padding: 0; box-sizing: border-box; }
  html, body { width: 825px; height: 1200px; overflow: hidden; background: var(--paper); }
  .sign { position: relative; width: 825px; height: 1200px; overflow: hidden; background: var(--paper); }
  .backdrop { position: absolute; inset: 0; }

  .brand { position: absolute; left: 417px; top: 46px; display: flex; align-items: center; gap: 14px; }
  .brand-square { width: 60px; height: 60px; background: var(--forest); }
  .brand-name { font-family: 'Montserrat', sans-serif; font-weight: 500; color: var(--forest); line-height: 1; }
  .brand-name .primary { display: block; font-size: 40px; letter-spacing: 1px; }
  .brand-name .secondary { display: block; font-size: 14px; letter-spacing: 11px; margin-top: 8px; }

  .headline { position: absolute; inset: 0; pointer-events: none; }
  .headline span { position: absolute; line-height: 1; white-space: nowrap; }
  .block-word { font-family: 'Oswald', sans-serif; font-weight: 500; font-size: 86px; letter-spacing: 12px; }
  .script-word { font-family: 'Dancing Script', cursive; font-weight: 700; }
  .new-one { left: 138px; top: 358px; color: var(--leaf-green); }
  .year { left: 138px; top: 420px; font-size: 104px; color: var(--leaf-green); }
  .new-two { left: 252px; top: 516px; color: var(--teal); }
  .you { left: 248px; top: 592px; font-size: 108px; color: var(--teal); }

  .benefits { position: absolute; left: 385px; top: 738px; width: 320px; list-style: none; }
  .benefits li { display: flex; gap: 14px; margin-bottom: 14px; font-family: 'Roboto Condensed', sans-serif; font-weight: 300; font-size: 20px; line-height: 1.2; color: var(--ink); }
  .benefits svg { flex: none; width: 22px; height: 20px; margin-top: 2px; }

  .retailer { position: absolute; left: 62px; top: 1068px; display: flex; align-items: center; gap: 10px; }
  .retailer-square { width: 22px; height: 22px; background: var(--brick); }
  .retailer-name { font-family: 'Montserrat', sans-serif; font-weight: 500; font-size: 15px; line-height: 1.2; color: var(--brick); }
</style>
</head>
<body>
<main class="sign">
  <svg class="backdrop" width="825" height="1200" viewBox="0 0 825 1200">
    <defs>
      <linearGradient id="tone-monstera" x1="0" y1="0" x2="1" y2="1">
        <stop offset="0" stop-color="#eef1ef"/><stop offset="0.6" stop-color="#c9d3c6"/><stop offset="1" stop-color="#2f4a2a"/>
      </linearGradient>
      <linearGradient id="tone-croton" x1="0" y1="0" x2="1" y2="1">
        <stop offset="0" stop-color="#eef0ee"/><stop offset="0.5" stop-color="#e2d6c3"/><stop offset="1" stop-color="#b88c6c"/>
      </linearGradient>
      <linearGradient id="tone-watering" x1="0" y1="0" x2="1" y2="1">
        <stop offset="0" stop-color="#e9e7e4"/><stop offset="0.5" stop-color="#8f9bab"/><stop offset="1" stop-color="#7cc9c6"/>
      </linearGradient>
    </defs>

    <!-- flowing lines -->
    <path d="M283 0 C300 110 380 170 490 172" fill="none" stroke="var(--line-yellow)" stroke-width="1.2"/>
    <path d="M490 172 C620 166 760 200 825 300" fill="none" stroke="var(--teal-light)" stroke-width="1.2"/>

    <!-- sun circle -->
    <circle cx="800" cy="672" r="112" fill="var(--sun-yellow)"/>
    <circle cx="808" cy="680" r="112" fill="none" stroke="var(--teal-light)" stroke-width="1"/>

    <!-- photo: woman misting monstera -->
    <circle cx="174" cy="278" r="142" fill="none" stroke="var(--leaf-green)" stroke-width="1"/>
    <circle cx="182" cy="270" r="134" fill="url(#tone-monstera)" role="img" aria-label="Photo of a smiling woman misting a monstera plant"/>

    <!-- photo: woman holding croton -->
    <circle cx="585" cy="415" r="190" fill="none" stroke="var(--teal-light)" stroke-width="1"/>
    <circle cx="572" cy="430" r="182" fill="url(#tone-croton)" role="img" aria-label="Photo of a woman holding a potted croton plant in a woven basket"/>
    <circle cx="575" cy="420" r="165" fill="none" stroke="var(--line-yellow)" stroke-width="1"/>

    <!-- photo: mother and daughter watering -->
    <circle cx="150" cy="845" r="150" fill="none" stroke="var(--teal-light)" stroke-width="1"/>
    <circle cx="138" cy="853" r="143" fill="url(#tone-watering)" role="img" aria-label="Photo of a mother and daughter watering a snake plant"/>

    <!-- grid accent -->
    <g stroke="var(--line-yellow)" stroke-width="1.2">
      <line x1="188" y1="1023" x2="272" y2="1023"/>
      <line x1="195" y1="1048" x2="260" y2="1048"/>
      <line x1="208" y1="1066" x2="294" y2="1066"/>
      <line x1="208" y1="1016" x2="208" y2="1080"/>
      <line x1="254" y1="1008" x2="254" y2="1070"/>
      <line x1="280" y1="1030" x2="280" y2="1097"/>
    </g>

    <!-- base mound and lines -->
    <circle cx="534" cy="1210" r="125" fill="var(--sage)"/>
    <path d="M425 1200 C450 1130 520 1100 570 1115 C600 1125 620 1160 632 1200" fill="none" stroke="var(--teal-light)" stroke-width="1"/>
    <path d="M578 1130 C650 1100 740 1078 825 1078" fill="none" stroke="var(--line-yellow)" stroke-width="1"/>
    <path d="M228 1110 C260 1140 300 1180 330 1200" fill="none" stroke="var(--line-yellow)" stroke-width="1"/>
  </svg>

  <div class="brand">
    <div class="brand-square"></div>
    <div class="brand-name"><span class="primary">VERDANT</span><span class="secondary">ROOTS</span></div>
  </div>

  <h1 class="headline" aria-label="New Year, New You!">
    <span class="block-word new-one">NEW</span>
    <span class="script-word year">year</span>
    <span class="block-word new-two">NEW</span>
    <span class="script-word you">you!</span>
  </h1>

  <ul class="benefits">
    <li><svg viewBox="0 0 22 20"><path d="M1 4 C8 0 18 2 21 17 C12 17 3 13 1 4 Z" fill="var(--teal-light)"/></svg>Houseplants give you a taste of nature.</li>
    <li><svg viewBox="0 0 22 20"><path d="M1 4 C8 0 18 2 21 17 C12 17 3 13 1 4 Z" fill="var(--teal-light)"/></svg>Houseplants boost air quality inside your home.</li>
    <li><svg viewBox="0 0 22 20"><path d="M1 4 C8 0 18 2 21 17 C12 17 3 13 1 4 Z" fill="var(--teal-light)"/></svg>Indoor plants reduce anxiety.</li>
    <li><svg viewBox="0 0 22 20"><path d="M1 4 C8 0 18 2 21 17 C12 17 3 13 1 4 Z" fill="var(--teal-light)"/></svg>Indoor plants make you more productive.</li>
    <li><svg viewBox="0 0 22 20"><path d="M1 4 C8 0 18 2 21 17 C12 17 3 13 1 4 Z" fill="var(--teal-light)"/></svg>Houseplants improve your concentration and memory.</li>
  </ul>

  <div class="retailer">
    <div class="retailer-square"></div>
    <div class="retailer-name">The Brickfield<br>Yard</div>
  </div>
</main>
</body>
</html>
```